Recruitment Agency in Texas, needs a stand out header letter

Our colours are red and grey and can be found on our website
just my logo will be sufficient and address...

Target Market(s)

Engineering Manufacturing

Colors
0094D4
00A9DD
6FCCEA
C7EBF8
E9F6FB
EB3D1F
EC4F4E
F09395
F8D3D4
FCEDEE

Requirements
Must have
• use colors red and grey
Should not have
• Please use same colors and font as my logo. My website is kelbrantstaffing.net

```html
<!DOCTYPE html>
<html lang="en">
<head>
<meta charset="utf-8">
<title>KelbrantStaffing Letterhead</title>
<link rel="stylesheet" href="https://fonts.googleapis.com/css2?family=Open+Sans:wght@400&family=Roboto:wght@400;500&display=swap">
<style>
  :root {
    --backdrop: #dcdcdc;
    --paper: #f8f8f8;
    --brand-red: #d21f2a;
    --brand-grey: #626266;
    --ink: #4b4b4b;
    --ink-dark: #3c3c3c;
  }
  * { margin: 0; padding: 0; box-sizing: border-box; }
  html, body {
    width: 1153px;
    height: 1200px;
    overflow: hidden;
    background: var(--backdrop);
  }
  .letterhead {
    position: absolute;
    left: 160px;
    top: 20px;
    width: 832px;
    height: 1160px;
    background: var(--paper);
    color: var(--ink);
    font-family: "Open Sans", Arial, sans-serif;
  }
  .brand-name {
    position: absolute;
    left: 75px;
    top: 92px;
    font-family: "Roboto", Arial, sans-serif;
    font-weight: 500;
    font-size: 41px;
    letter-spacing: -0.5px;
    color: var(--brand-red);
    line-height: 1;
  }
  .office {
    position: absolute;
    left: 561px;
    top: 70px;
    font-family: "Roboto", Arial, sans-serif;
    font-size: 13px;
    color: var(--ink-dark);
    line-height: 18px;
  }
  .office-title { color: var(--brand-red); }
  .office-address { margin-bottom: 4px; }
  .contact-line {
    display: flex;
    align-items: center;
    gap: 5px;
  }
  .contact-line svg { width: 13px; height: 13px; flex: none; }
  .letter-body {
    position: absolute;
    left: 75px;
    top: 259px;
    width: 681px;
    font-size: 14.9px;
    line-height: 22.4px;
  }
  .letter-body p { margin-bottom: 22.4px; text-align: justify; }
  .letter-body .salutation,
  .letter-body .closing { text-align: left; }
  .signature-area {
    position: absolute;
    left: 75px;
    top: 847px;
    width: 97px;
    height: 91px;
    background: linear-gradient(135deg, #ececec, #e2e2e2);
  }
  .footer-band {
    position: absolute;
    left: 0;
    bottom: 0;
    width: 100%;
    height: 23px;
  }
  .footer-band .band-grey {
    position: absolute; left: 0; top: 0; width: 89px; height: 100%;
    background: var(--brand-grey);
  }
  .footer-band .band-red {
    position: absolute; left: 92px; right: 0; top: 0; height: 100%;
    background: var(--brand-red);
  }
</style>
</head>
<body>
  <main class="letterhead">
    <div class="brand-name">KelbrantStaffing</div>

    <address class="office" style="font-style: normal;">
      <div class="office-title">Houston Office</div>
      <div class="office-address">48 Larkfield Avenue Houston</div>
      <div class="contact-line">
        <svg viewBox="0 0 24 24" aria-hidden="true"><path fill="var(--brand-red)" d="M6.6 10.8c1.4 2.8 3.8 5.1 6.6 6.6l2.2-2.2c.3-.3.7-.4 1-.2 1.1.4 2.3.6 3.6.6.6 0 1 .4 1 1V20c0 .6-.4 1-1 1C10.6 21 3 13.4 3 4c0-.6.4-1 1-1h3.5c.6 0 1 .4 1 1 0 1.3.2 2.5.6 3.6.1.3 0 .7-.2 1z"/></svg>
        <span>(+1) 832-555-0186</span>
      </div>
      <div class="contact-line">
        <svg viewBox="0 0 24 24" aria-hidden="true"><rect x="2" y="5" width="20" height="14" fill="var(--brand-red)"/><path d="M2 5l10 8 10-8" fill="none" stroke="var(--paper)" stroke-width="2"/></svg>
        <span>info@kelbrantstaffing.net</span>
      </div>
      <div class="contact-line">
        <svg viewBox="0 0 24 24" aria-hidden="true"><g fill="none" stroke="var(--brand-red)" stroke-width="2"><circle cx="12" cy="12" r="9.5"/><ellipse cx="12" cy="12" rx="4" ry="9.5"/><path d="M2.5 12h19"/></g></svg>
        <span>www.kelbrantstaffing.net</span>
      </div>
    </address>

    <section class="letter-body">
      <p class="salutation">Dear customer,</p>
      <p>Lorem ipsum dolor sit amet, consectetur adipisicing elit, sed do eiusmod tempor incididunt ut labore et dolore magna aliqua. Ut enim ad minim veniam, quis nostrud exercitation ullamco laboris nisi ut aliquip ex ea commodo consequat. Duis aute irure dolor in reprehenderit in voluptate velit esse cillum dolore eu fugiat nulla pariatur. Excepteur sint occaecat cupidatat non proident, sunt in culpa qui officia deserunt mollit anim id est laborum.</p>
      <p>Lorem ipsum dolor sit amet, consectetur adipisicing elit, sed do eiusmod tempor incididunt ut labore et dolore magna aliqua. Ut enim ad minim veniam, quis nostrud exercitation ullamco laboris nisi ut aliquip ex ea commodo consequat. Duis aute irure dolor in reprehenderit in voluptate velit esse cillum dolore eu fugiat nulla pariatur. Excepteur sint occaecat cupidatat non proident, sunt in culpa qui officia deserunt mollit anim id est laborum.</p>
      <p>Lorem ipsum dolor sit amet, consectetur adipisicing elit, sed do eiusmod tempor incididunt ut labore et dolore magna aliqua. Ut enim ad minim veniam, quis nostrud exercitation ullamco laboris nisi ut aliquip ex ea commodo consequat. Duis aute irure dolor in reprehenderit in voluptate velit esse cillum dolore eu fugiat nulla pariatur. Excepteur sint occaecat cupidatat non proident, sunt in culpa qui officia deserunt mollit anim id est laborum.</p>
      <p>Lorem ipsum dolor sit amet, consectetur adipisicing elit, sed do eiusmod tempor incididunt ut labore et dolore magna aliqua. Ut enim ad minim veniam, quis nostrud exercitation ullamco laboris nisi ut aliquip ex ea commodo consequat. Duis aute irure dolor in reprehenderit.</p>
      <p class="closing">Yours Sincerely,</p>
    </section>

    <div class="signature-area" role="img" aria-label="Handwritten signature of the sender"></div>

    <div class="footer-band" aria-hidden="true">
      <div class="band-grey"></div>
      <div class="band-red"></div>
    </div>
  </main>
</body>
</html>
```